We need a single page A4, single sided pdf brochure to promote our business to other businesses. Parcelo Back provides international returns solutions to on line retailers. This includes local return addresses and labels to allow customers to quickly and easily send their unwarted items back. we hen ship the returns back in bulk to the retailer.

```html
<!DOCTYPE html>
<html lang="en">
<head>
<meta charset="utf-8">
<title>Parcelo Back – International Returns Solutions</title>
<link href="https://fonts.googleapis.com/css2?family=Lato:wght@400;700;900&family=Roboto:wght@700;900&display=swap" rel="stylesheet">
<style>
  :root {
    --orange: #e39210;
    --ink: #1c1c1c;
    --logo-ink: #2b2b2b;
    --panel-grey: #ececec;
    --footer: #2a2a2a;
    --backdrop: #808080;
    --white: #ffffff;
  }
  * { box-sizing: border-box; margin: 0; padding: 0; }
  html, body { width: 1200px; height: 1200px; overflow: hidden; }
  body { background: var(--backdrop); font-family: "Lato", sans-serif; color: var(--ink); position: relative; }

  .brochure {
    position: absolute; left: 201px; top: 40px;
    width: 797px; height: 1120px;
    background: var(--white); overflow: hidden;
  }
  .brochure > * { position: absolute; }

  .hero-art { left: 0; top: 0; width: 797px; height: 389px; }

  .brand { left: 33px; top: 50px; display: flex; align-items: center; gap: 14px; }
  .brand-mark { width: 34px; height: 34px; background: var(--orange); }
  .brand-name { font-family: "Lato", sans-serif; font-weight: 900; font-size: 43px; letter-spacing: 1px; color: var(--logo-ink); text-transform: uppercase; }

  .hero-title { left: 33px; top: 124px; font-family: "Roboto", sans-serif; text-transform: uppercase; }
  .hero-title .lead { display: block; font-weight: 900; font-size: 47px; color: var(--white); line-height: 52px; }
  .hero-title .sub { display: block; font-weight: 900; font-size: 28px; color: var(--ink); line-height: 34px; }
  .hero-copy { left: 34px; top: 268px; width: 360px; font-family: "Roboto", sans-serif; font-weight: 700; font-size: 17px; line-height: 22px; color: var(--white); }
  .hero-copy p + p { margin-top: 13px; }

  .services-band { left: 0; top: 397px; width: 797px; height: 306px; background: var(--panel-grey); }
  .section-heading { font-weight: 700; font-size: 20.5px; line-height: 25px; color: var(--orange); }
  .benefits { left: 31px; top: 404px; width: 345px; }
  .solutions { left: 412px; top: 410px; width: 360px; }
  .bullet-list { list-style: none; margin-top: 9px; }
  .bullet-list li { position: relative; padding-left: 14px; font-size: 15px; line-height: 19px; margin-bottom: 9px; }
  .bullet-list li::before { content: ""; position: absolute; left: 1px; top: 7px; width: 5px; height: 5px; border-radius: 50%; background: var(--orange); }
  .solutions .bullet-list li { font-size: 16px; line-height: 20px; margin-bottom: 8px; }
  .column-rule { left: 413px; top: 450px; width: 2px; height: 172px; background: var(--ink); }
  .countries-note { left: 414px; top: 602px; width: 360px; font-weight: 700; font-size: 17px; line-height: 22px; color: var(--orange); }

  .about { left: 34px; top: 712px; width: 733px; }
  .about h2 { font-weight: 700; font-size: 20px; color: var(--orange); line-height: 24px; }
  .about p { font-size: 13.2px; line-height: 17px; margin-bottom: 6px; }

  .contact-card { left: 0; top: 851px; width: 388px; height: 201px; background: var(--orange); border-radius: 0 16px 16px 0; padding: 5px 0 0 34px; color: var(--white); }
  .contact-card h2 { font-weight: 700; font-size: 20px; line-height: 24px; }
  .contact-card .line { font-size: 14px; line-height: 22px; display: flex; align-items: center; gap: 5px; }
  .contact-card .prompt { font-weight: 700; }
  .contact-card .phone { font-weight: 900; font-size: 18px; margin-top: 4px; }
  .contact-card svg { flex: none; }

  .courier-photo { left: 452px; top: 838px; width: 250px; height: 221px; background: radial-gradient(ellipse at 50% 45%, #2b5fc9 0%, #3d6fd6 30%, #c9a57a 62%, #ffffff 80%); }

  .footer-bar { left: 0; top: 1059px; width: 797px; height: 61px; background: var(--footer); display: flex; align-items: center; justify-content: center; gap: 8px; color: var(--white); font-size: 15px; letter-spacing: 4px; }
</style>
</head>
<body>
  <main class="brochure">
    <svg class="hero-art" viewBox="0 0 797 389" aria-hidden="false">
      <defs>
        <linearGradient id="shopperTones" x1="0" y1="0" x2="1" y2="1">
          <stop offset="0" stop-color="#f4eee6"/>
          <stop offset="0.45" stop-color="#e8d2bc"/>
          <stop offset="0.75" stop-color="#3f86c7"/>
          <stop offset="1" stop-color="#2c5f99"/>
        </linearGradient>
      </defs>
      <polygon points="471,0 797,0 797,28 464,28" fill="#e39210"/>
      <polygon points="464,28 797,28 797,389 405,389" fill="url(#shopperTones)" role="img" aria-label="Photo of a smiling woman shopping online with a laptop and bank card"/>
      <polygon points="0,115 430,115 383,389 0,389" fill="#e39210"/>
      <polygon points="437,115 447,115 401,389 391,389" fill="#e39210"/>
    </svg>

    <div class="brand">
      <span class="brand-mark"></span>
      <span class="brand-name">Parcelo Back</span>
    </div>

    <h1 class="hero-title">
      <span class="lead">International</span>
      <span class="sub">Returns Solutions for</span>
      <span class="sub">On-line Retailers</span>
    </h1>
    <div class="hero-copy">
      <p>Selling internationally brings opportunities and challenges to retailers of all sizes.</p>
      <p>One of those challenges is how to deal effectively with customer returns.</p>
    </div>

    <div class="services-band"></div>

    <section class="benefits">
      <h2 class="section-heading">Parcelo Back have a range of services to suit retailers of all sizes that will:</h2>
      <ul class="bullet-list">
        <li>Lower your returns costs – Save you and your customers money</li>
        <li>Improve your customers experience–Better feedback &amp; ratings</li>
        <li>Add value to your international business– More Sales</li>
        <li>Save time on managing International Returns – Less Administration</li>
        <li>Help you comply with marketplace International Return policies and best practice</li>
      </ul>
    </section>

    <div class="column-rule"></div>

    <section class="solutions">
      <h2 class="section-heading">Our Solution includes:</h2>
      <ul class="bullet-list">
        <li>Local Returns Addresses in 9 Countries*</li>
        <li>Return Label solutions in over 20 other countries*</li>
        <li>Your own dedicated &amp; branded Label Portal</li>
        <li>Parcelo Back Retailer Portal to monitor and manage your returns</li>
      </ul>
    </section>
    <p class="countries-note">*Please see our website for an up-to-date list of countries we operate in.</p>

    <section class="about">
      <h2>About Us</h2>
      <p>Parcelo Back is a fast growing family-run business that has been providing International return services to on line sellers since 2015. Through our UK and French based businesses, together with our trusted partner network, we deliver a service that saves retailers money and time.</p>
      <p>The owners of Parcelo Back come from a retail and e-commerce background, so we fully understand and appreciate the issues and challenges faced by retailers, as well as the concerns of customers when it comes to returns.</p>
    </section>

    <section class="contact-card">
      <h2>Interested?</h2>
      <div class="line prompt">See our website for more information</div>
      <div class="line">
        <svg width="12" height="12" viewBox="0 0 12 12"><circle cx="6" cy="6" r="5" fill="none" stroke="#fff" stroke-width="1.2"/><ellipse cx="6" cy="6" rx="2.2" ry="5" fill="none" stroke="#fff" stroke-width="1"/><line x1="1" y1="6" x2="11" y2="6" stroke="#fff" stroke-width="1"/></svg>
        www.parceloback.example
      </div>
      <div class="line prompt">or contact us to discuss how we can work together.</div>
      <div class="line">
        <svg width="12" height="9" viewBox="0 0 12 9"><rect x="0.5" y="0.5" width="11" height="8" fill="none" stroke="#fff"/><polyline points="0.5,0.5 6,5 11.5,0.5" fill="none" stroke="#fff"/></svg>
        info@parceloback.example
      </div>
      <div class="line prompt">Write to us in these languages</div>
      <div class="line">EN &nbsp; DE &nbsp; ES &nbsp;FR &nbsp;(Flags)</div>
      <div class="line phone">
        <svg width="15" height="15" viewBox="0 0 16 16"><circle cx="8" cy="8" r="7" fill="none" stroke="#fff" stroke-width="1.3"/><path d="M5.5 4.5 L7 4.5 L7.5 6.5 L6.6 7.2 Q7.5 9 9 9.6 L9.7 8.7 L11.5 9.2 L11.5 10.7 Q8.5 11.5 6 9 Q4.5 7 5.5 4.5 Z" fill="#fff"/></svg>
        +44(0)161 555 0192
      </div>
    </section>

    <div class="courier-photo" role="img" aria-label="Photo of a delivery courier in blue uniform holding a clipboard and parcels"></div>

    <footer class="footer-bar">
      <svg width="13" height="13" viewBox="0 0 12 12"><circle cx="6" cy="6" r="5" fill="none" stroke="#fff" stroke-width="1.2"/><ellipse cx="6" cy="6" rx="2.2" ry="5" fill="none" stroke="#fff" stroke-width="1"/><line x1="1" y1="6" x2="11" y2="6" stroke="#fff" stroke-width="1"/></svg>
      <span>www.parceloback.example</span>
    </footer>
  </main>
</body>
</html>
```